Poster Design - Stand Up Paddle Eco Tour

We need a A3 size poster design (using Adobe Illustrator) for our company's stand up paddle tour. Our tour is on flat water, calm and safe, suitable for all ages and level.

WE provide worldclass SUP boards for our customers. And branded Tovar Helsby life jacket. Our instructors are all well trained and exeprience. Plus they are super friendly. Every paddling trip come with a safety boat.

Please refer to attached files for text and photos.

Our website is www.brimwakeglide.com.sg

IMPORTANT NOTE - The design has to be done in Adobe Illustrator. The winning designer has to submit the working file in Adobe Illustrator.

Target Market(s)

Working adult - 20 - 35 year old

Industry/Entity Type

Tourism

Requirements
Must have
• The project MUST be done in Adobe Illustrator and the winning designer has to submit the artwork to us in Adobe Illustrator format.
Nice to have
• pleasant to look at.

```html
<!DOCTYPE html>
<html lang="en">
<head>
<meta charset="utf-8">
<title>Brimwake Glide – SUP Eco Tour Poster</title>
<link rel="stylesheet" href="https://fonts.googleapis.com/css2?family=Oswald:wght@500;600&family=Righteous&display=swap">
<style>
  :root {
    --paper: #f6f46e;
    --red: #f0194f;
    --orange: #f7941d;
    --ink: #111111;
    --cyan: #2fd9ee;
    --navy: #1d3557;
    --band-a: #fbe325;
    --band-b: #f7941d;
    --band-c: #ee2a3a;
  }
  * { margin: 0; padding: 0; box-sizing: border-box; }
  html, body { width: 849px; height: 1200px; overflow: hidden; }
  body { background: var(--paper); position: relative; font-family: "Oswald", sans-serif; }

  .band { position: absolute; left: 0; width: 849px;
    background: linear-gradient(90deg, var(--band-a) 0%, var(--band-b) 60%, var(--band-c) 100%); }
  .band--top { top: 0; height: 12px; }
  .band--bottom { bottom: 0; height: 26px; }

  .headline, .subhead, .tagline, .intro, .pitch, .details, .notice, .contact { position: absolute; left: 0; width: 849px; text-align: center; }

  .headline { top: 24px; font-weight: 600; font-size: 72px; color: var(--red); line-height: 1.2; }
  .subhead { top: 132px; font-weight: 600; font-size: 36px; color: var(--orange); line-height: 1.2; padding-right: 40px; }
  .tagline { top: 182px; font-weight: 600; font-size: 38px; color: var(--ink); line-height: 1.2; padding-right: 20px; }

  .intro { top: 236px; padding: 0 50px 0 60px; font-weight: 500; font-size: 22px; line-height: 1.4; color: var(--red); }
  .pitch { top: 342px; padding: 0 60px 0 40px; font-weight: 500; font-size: 22px; line-height: 1.4; color: var(--orange); }

  .details { top: 484px; font-family: "Righteous", sans-serif; font-size: 26px; line-height: 1.22; color: var(--ink); }
  .details p + p { margin-top: 4px; }

  .photo { position: absolute; }
  .photo--mangrove { left: 22px; top: 628px; width: 378px; height: 170px;
    background: linear-gradient(180deg, #d7e9f3 0%, #4f8a3d 30%, #2f6a2c 72%, #7c8a6b 100%); }
  .photo--paddlers { left: 456px; top: 628px; width: 367px; height: 170px;
    background: linear-gradient(180deg, #cfe4f1 0%, #3f7436 38%, #7a8569 62%, #8d9380 100%); }
  .photo--group { left: 241px; top: 816px; width: 362px; height: 168px;
    background: linear-gradient(180deg, #eef3f8 0%, #9dc1dc 22%, #3d7334 45%, #6f7c62 70%, #8a8f7e 100%); }

  .notice { top: 990px; font-family: "Righteous", sans-serif; font-size: 21px; color: var(--ink); }

  .brand { position: absolute; left: 14px; top: 1030px; width: 124px; height: 124px;
    display: flex; flex-direction: column; align-items: center; justify-content: center; gap: 6px; }
  .brand__dot { width: 18px; height: 18px; border-radius: 50%; background: var(--navy); }
  .brand__name { font-family: "Righteous", sans-serif; font-size: 20px; line-height: 1.1; color: var(--navy); text-align: center; }

  .contact { font-family: "Righteous", sans-serif; color: var(--ink); }
  .contact--web { top: 1030px; font-size: 22px; color: var(--cyan); text-decoration: underline; padding-left: 2px; }
  .contact--social { top: 1070px; font-size: 22px; text-decoration: underline; padding-left: 14px; }
  .contact--label { top: 1112px; font-size: 22px; text-decoration: underline; }
  .contact--email { top: 1140px; font-size: 22px; text-decoration: underline; }
</style>
</head>
<body>
  <div class="band band--top"></div>

  <h1 class="headline">Explore the natural</h1>
  <h2 class="subhead">coastal surroundings and waterways</h2>
  <h2 class="tagline">of Johor on a SUP adventure touring board</h2>

  <p class="intro">Our tours are flat-water and appropriate for all ages and levels. We have the best possible service and equipment. Join us for a fun and relaxing day.</p>
  <p class="pitch">What could be better than a group guided tour? With life vests and a safety boat for our guided tour, you can be assured of a secured environment while you focus on just having fun and creating life’s best memories with friends and family.</p>

  <div class="details">
    <p>Timing: Morning, afternoon, and<br>sunset session</p>
    <p>Location: Kim Kim River, set off from Teluk<br>Kabong, Pasir Gudang. (next to Pasir Putih)</p>
  </div>

  <div class="photo photo--mangrove" role="img" aria-label="Paddler on calm river beside dense mangrove trees"></div>
  <div class="photo photo--paddlers" role="img" aria-label="Two paddlers standing on long yellow touring boards near mangroves"></div>
  <div class="photo photo--group" role="img" aria-label="Group of paddlers on a mangrove river under a cloudy sky"></div>

  <p class="notice">Contact us for booking. We do not accept walk-in.</p>

  <div class="brand">
    <span class="brand__dot"></span>
    <span class="brand__name">Brimwake<br>Glide</span>
  </div>

  <p class="contact contact--web">http://brimwakeglide.com.sg/</p>
  <p class="contact contact--social">Social: Brimwake Glide</p>
  <p class="contact contact--label">Booking Contact:</p>
  <p class="contact contact--email">booking@brimwakeglide.com.sg</p>

  <div class="band band--bottom"></div>
</body>
</html>
```